Spiritual Self Help Book Cover

I need a book cover that's extremely appealing to spiritual seekers, self-help/health and wellness fans. Mostly for women.
The book blends spirituality/mysticism with science for readers to understand how to optimize their health/body, emotional well-being, mental wellness, spiritual fulfillment, relationships, business and purpose in life. It infuses ancient and modern understanding of energy/frequency/quantum mechanics along with the science of chiropractic and psychology.
Book title: Folding Every Lantern Inward
I'll attach some examples that are similar to what I like but I want something different and more extravagantly beautiful.
Please use the graphic of the Sri Yantra Mandala into the cover instead of this stock image one.
I'll need the book cover in all formats: paperback, hardcover, ebook and audiobook.
I'll provide the rest of the details, including publisher logo, synopsis, author photo/blurb and ISBN after I pick the final wniner.
Mostly women spiritual seekers, self-help readers, health/wellness enthusiasts

```html
<!DOCTYPE html>
<html lang="en">
<head>
<meta charset="utf-8">
<title>Folding Every Lantern Inward — Book Cover</title>
<link rel="stylesheet" href="https://fonts.googleapis.com/css2?family=Cinzel:wght@400;500&display=swap">
<style>
  :root {
    --backdrop: #bbbcbe;
    --paper: #ffffff;
    --space-deep: #141d45;
    --space-blue: #3a4a93;
    --space-violet: #7a5aa6;
    --nebula-pink: #c4668f;
    --core-glow: #fbf7ff;
    --haze: #9a98aa;
    --gold-light: #fff36a;
    --gold: #f2c500;
    --gold-deep: #b98a00;
    --bevel: #4a2a08;
  }
  * { margin: 0; padding: 0; box-sizing: border-box; }
  html, body {
    width: 1200px;
    height: 1200px;
    overflow: hidden;
    background: var(--backdrop);
  }
  .cover {
    position: absolute;
    left: 230px;
    top: 44px;
    width: 741px;
    height: 1111px;
    background: var(--paper);
    overflow: hidden;
  }
  .cosmos {
    position: absolute;
    inset: 0;
    width: 100%;
    height: 100%;
  }
  .title {
    position: absolute;
    left: 0;
    right: 0;
    text-align: center;
    font-family: "Cinzel", serif;
    font-weight: 400;
    line-height: 1;
    white-space: nowrap;
  }
  .title-line {
    position: absolute;
    left: 0;
    right: 0;
    background: linear-gradient(180deg, var(--gold-light) 0%, var(--gold) 45%, var(--gold-deep) 100%);
    -webkit-background-clip: text;
    background-clip: text;
    color: transparent;
    filter: drop-shadow(-2px 2px 0 var(--bevel)) drop-shadow(-1px 1px 0 var(--bevel));
  }
  .title-line.major { font-size: 108px; letter-spacing: 1px; }
  .title-line.minor { font-size: 58px; letter-spacing: 2px; }
  .line-1 { top: 600px; }
  .line-2 { top: 708px; }
  .line-3 { top: 778px; }
  .line-4 { top: 882px; }
  .author {
    position: absolute;
    left: 0;
    right: 0;
    top: 1033px;
    text-align: center;
    font-family: "Cinzel", serif;
    font-size: 23px;
    letter-spacing: 9px;
    color: var(--gold);
    text-shadow: -1px 1px 0 var(--gold-deep);
  }
</style>
</head>
<body>
  <main class="cover">
    <svg class="cosmos" viewBox="0 0 741 1111" role="img" aria-label="Illustration of a violet and pink spiral galaxy with a bright glowing core and a bright star, overlaid with a fine sacred geometry line pattern, fading diagonally into white">
      <defs>
        <linearGradient id="space-base" x1="0" y1="0" x2="0.3" y2="1">
          <stop offset="0" stop-color="var(--space-deep)"/>
          <stop offset="0.35" stop-color="var(--space-blue)"/>
          <stop offset="0.7" stop-color="var(--space-violet)"/>
          <stop offset="1" stop-color="var(--haze)"/>
        </linearGradient>
        <radialGradient id="nebula" cx="0.85" cy="0.42" r="0.6">
          <stop offset="0" stop-color="var(--core-glow)"/>
          <stop offset="0.12" stop-color="#f1d8ec"/>
          <stop offset="0.35" stop-color="var(--nebula-pink)" stop-opacity="0.8"/>
          <stop offset="1" stop-color="var(--nebula-pink)" stop-opacity="0"/>
        </radialGradient>
        <linearGradient id="fade-white" x1="0" y1="0" x2="0.35" y2="1">
          <stop offset="0.45" stop-color="#ffffff" stop-opacity="0"/>
          <stop offset="0.72" stop-color="#ffffff" stop-opacity="0.9"/>
          <stop offset="0.8" stop-color="#ffffff" stop-opacity="1"/>
        </linearGradient>
        <clipPath id="space-area">
          <polygon points="0,0 741,0 741,820 0,460"/>
        </clipPath>
      </defs>
      <g clip-path="url(#space-area)">
        <rect width="741" height="1111" fill="url(#space-base)"/>
        <rect width="741" height="1111" fill="url(#nebula)"/>
        <rect width="741" height="1111" fill="url(#fade-white)"/>
      </g>
    </svg>

    <h1 class="title">
      <span class="title-line major line-1">FOLDING</span>
      <span class="title-line minor line-2">EVERY</span>
      <span class="title-line major line-3">LANTERN</span>
      <span class="title-line major line-4">INWARD</span>
    </h1>

    <p class="author">DR. MIRIAM CALLOWAY</p>
  </main>
</body>
</html>
```